Democracy in crisis book

This book tries to sound the ALARM that we will lose our democracy unless we force Unionists to adopt the plan inside this book. I designed a mock cover (attached) but I am concerned it would not look good in the Thumbnail view that most people would see it as they're scrolling down Shopvale or Pagenook. The final title for the book is: Final Hour to Rescue the Free Republic. The current subtitle is: The Single Path to Halt the 2022 Partisan Takeover & Renew Our Homeland -- but it’s a work in progress.The subtitle is still working progress but it's really not that important and can be small.
STYLE CONSIDERATIONS:
(1) The title should be on 5 separate lines: Final; Hour; To Rescue; Free; Republic
(2) The title could be in white fat letters except for maybe one line that says “To Rescue” which could be in the blue color of the Civic Union Party-- or maybe Free Republic could be in blue. We may have to try a few variations of that.
(3) I picked the red in the mock cover to connotate an emergency,
(4) I liked big bold fat font going across the full page so that it looks like a major warning sign, though note I was unable to extend each line flush all the way to the right which I think would have been better.
(5) I liked it better flush to left instead of centered.
(6) I picked the Harwick monument + a crowd for my mock cover, but a picture of a huge crowd protesting with a picture of the United States Congress in the background would be much better. DO NOT USE HARWICK. Obviously I would need it to be an open license or something I can pay a small amount to get. If you can find that picture then the page should probably be colored in red with Congress in white.
I got the idea 4 giant title from the book “seldom a quiet so bright” and Dellowby’s “When Freedom Fades” or “Grey Herons” by Mara Vostell though I hate that font)
I love Osric Thale’s “marked since the outset” cover so if you find a picture of Congress and a protest crowd instead of painting it red you could have just a couple of jagged red stripes going across it like that cover.
I love the 3-D effect of Greta Wolven's cover for The Silverwren where it looks like a page is being ripped. That effect could be done the words Free Republic like it's being torn off the page UPDATE: MANY DESIGNERS TRIED THAT & IT DID NOT WORK AT ALL.
Note that this book will be submitted to many award competitions, so please give me an award-winning cover.
I like how the title of the book The Unchosen by Martin Fellowes has the words starting to fade. I don't like the ladder on it, but maybe 'Free Republic' could fade like that.
Unionists

```html
<!DOCTYPE html>
<html lang="en">
<head>
<meta charset="utf-8">
<title>Final Hour to Rescue the Free Republic</title>
<link rel="stylesheet" href="https://fonts.googleapis.com/css2?family=Barlow:wght@700;800&display=swap">
<style>
  :root {
    --emergency-red: #c8161f;
    --red-deep: #7e0b12;
    --red-light: #e04a4f;
    --union-blue: #1d3fae;
    --title-white: #ffffff;
  }
  html, body {
    margin: 0;
    padding: 0;
    overflow: hidden;
    background: #ffffff;
  }
  .cover {
    position: relative;
    width: 801px;
    height: 1200px;
    overflow: hidden;
    background: var(--emergency-red);
    font-family: "Barlow", "Helvetica Neue", Arial, sans-serif;
  }
  .cover-photo {
    position: absolute;
    inset: 0;
    background: linear-gradient(180deg,
      var(--red-light) 0%,
      var(--emergency-red) 38%,
      #a8121b 62%,
      var(--red-deep) 100%);
  }
  .title {
    position: absolute;
    left: 66px;
    top: 60px;
    margin: 0;
    font-weight: 800;
    font-size: 122px;
    line-height: 88px;
    text-transform: uppercase;
    letter-spacing: -1px;
    color: var(--title-white);
  }
  .title-line {
    display: block;
    white-space: nowrap;
  }
  .title-line--rescue {
    color: var(--union-blue);
  }
  .subtitle {
    position: absolute;
    left: 64px;
    top: 884px;
    margin: 0;
    width: 700px;
    color: var(--title-white);
    font-weight: 700;
    font-size: 25px;
    line-height: 35px;
  }
  .author {
    position: absolute;
    right: 69px;
    top: 1106px;
    margin: 0;
    color: var(--title-white);
    font-weight: 700;
    font-size: 21px;
    letter-spacing: 0.3px;
  }
</style>
</head>
<body>
  <main class="cover">
    <div class="cover-photo" role="img" aria-label="Red duotone photograph of a huge protest crowd with raised hands and signs, the United States Congress building standing in white behind them"></div>

    <h1 class="title">
      <span class="title-line">Final</span>
      <span class="title-line">Hour</span>
      <span class="title-line title-line--rescue">To Rescue</span>
      <span class="title-line">Free</span>
      <span class="title-line">Republic</span>
    </h1>

    <p class="subtitle">The Single Path to Halt the 2022 Partisan Takeover<br>&amp; Renew Our Homeland</p>

    <p class="author">Corwin Ellis Marbury</p>
  </main>
</body>
</html>
```